Lumora Vitality MediSpa Brochure

We need a new brochure design. The old is attached.

We are wanting a three panel brochure for med spa designed and ready for print. The brochure will have content and images on both sides. We attached the old brochure in pdf format. The content needs to stay as on the attached pdf but please feel free to offer new designs. The color needs to match the attached logo, which is a light blue and teal. All images we want on the brochure are also attached.

The design must have an 1/8 in space from each edge for printing purposes

Target Market(s)

Men and Women

Industry/Entity Type

Wellness

Font styles to use
Sans Serif

Colors
34a6d7
33b8a4

Requirements
Must have
• soft curves. must have a 1/8 in space on all edges (including interior) to give bleed space for printing. Use content written on attached brochure.

```html
<!DOCTYPE html>
<html lang="en">
<head>
<meta charset="utf-8">
<title>Lumora Vitality MediSpa Brochure</title>
<link href="https://fonts.googleapis.com/css2?family=Montserrat:wght@500;600;700&family=Open+Sans:ital,wght@0,400;0,600;0,700;1,400;1,600&display=swap" rel="stylesheet">
<style>
:root{
  --teal:#33b8a4;
  --teal-deep:#1f9c8a;
  --teal-dark:#17806f;
  --blue:#34a6d7;
  --blue-light:#5cc0e8;
  --ink:#333b3f;
  --grey:#5b6064;
  --paper:#f3f5f5;
  --bg:#e4e6e7;
}
*{box-sizing:border-box;margin:0;padding:0}
html,body{width:902px;height:1200px;overflow:hidden;background:var(--bg)}
body{font-family:"Open Sans",Arial,sans-serif;color:var(--ink);position:relative}
.spread{position:absolute;left:21px;width:860px;height:558px;background:var(--paper);overflow:hidden;box-shadow:0 4px 14px rgba(0,0,0,.18)}
.spread--outside{top:28px}
.spread--inside{top:614px}
.spread-art{position:absolute;inset:0;width:860px;height:558px}
.panel{position:absolute;top:0;width:286.67px;height:558px}
.panel--1{left:0}.panel--2{left:286.67px}.panel--3{left:573.33px}
.abs{position:absolute}
.body-text{font-size:8.3px;line-height:1.38;text-align:justify;color:var(--ink)}
.pill{position:absolute;left:0;height:15px;padding:0 18px 0 16px;border-radius:0 9px 9px 0;background:linear-gradient(90deg,var(--blue),var(--blue-light));color:#fff;font-family:"Montserrat",sans-serif;font-weight:600;font-size:7.6px;line-height:15px;letter-spacing:.2px}
.pill--teal{background:var(--teal);border-radius:9px;padding:0 14px}
.tab{position:absolute;top:0;left:50%;transform:translateX(-50%);width:190px;height:32px;border-radius:0 0 8px 8px;background:linear-gradient(180deg,var(--teal),var(--teal-deep));color:#fff;font-family:"Montserrat",sans-serif;font-weight:600;font-size:9.4px;text-align:center;line-height:32px;box-shadow:0 3px 4px rgba(0,0,0,.15)}
.tab--mid{top:auto;border-radius:8px;height:28px;line-height:28px;width:200px}
.dot-list{list-style:none;font-size:8px;font-style:italic;font-weight:600}
.dot-list li{position:relative;padding-left:14px;margin-bottom:6px}
.dot-list li::before{content:"";position:absolute;left:0;top:3px;width:6px;height:6px;border-radius:50%;background:var(--teal)}
.tick-list{list-style:none;font-size:7px;font-style:italic;font-weight:600}
.tick-list li{position:relative;padding-left:14px;margin-bottom:5px}
.tick-list li::before{content:"";position:absolute;left:1px;top:1px;width:6px;height:3px;border-left:1.5px solid var(--teal);border-bottom:1.5px solid var(--teal);transform:rotate(-45deg)}
.brand{display:flex;align-items:center;justify-content:center;gap:6px;font-family:"Open Sans",sans-serif;font-weight:600;color:var(--teal);white-space:nowrap}
.brand-dot{width:10px;height:10px;border-radius:50%;background:var(--teal)}
.photo{position:absolute}
.label-teal{font-family:"Montserrat",sans-serif;font-weight:600;font-size:7.6px;color:var(--teal-deep)}
.contact{font-size:7.6px;line-height:1.5;display:flex;gap:5px;align-items:flex-start}
.contact svg{flex:none;margin-top:2px}
.white{color:#fff}
</style>
</head>
<body>

<section class="spread spread--outside">
  <svg class="spread-art" viewBox="0 0 860 558" aria-hidden="true">
    <defs>
      <linearGradient id="p1bg" x1="0" x2="1"><stop offset="0" stop-color="#dceff7"/><stop offset="1" stop-color="#ffffff"/></linearGradient>
      <linearGradient id="tealg" x1="0" x2="1"><stop offset="0" stop-color="#22a593"/><stop offset="1" stop-color="#3cc1ad"/></linearGradient>
      <linearGradient id="swoosh" x1="0" x2="1"><stop offset="0" stop-color="#3a3d40"/><stop offset="1" stop-color="#a3a7aa"/></linearGradient>
    </defs>
    <rect x="0" y="0" width="287" height="558" fill="url(#p1bg)"/>
    <rect x="287" y="0" width="287" height="558" fill="#f2f4f4"/>
    <rect x="573" y="0" width="287" height="558" fill="#f3f4f4"/>
    <path d="M0 0H287V18C210 62 110 26 0 58Z" fill="url(#tealg)"/>
    <path d="M0 62C110 32 210 58 287 24V32C210 66 110 42 0 72Z" fill="#ffffff" opacity=".7"/>
    <path d="M0 466C90 430 200 440 287 452V466C200 458 90 462 0 496Z" fill="#34a6d7"/>
    <path d="M0 496C90 462 200 458 287 466V476C200 472 100 478 0 512Z" fill="#ffffff"/>
    <rect x="0" y="518" width="287" height="40" fill="#48bfae"/>
    <path d="M287 0H500C440 20 360 36 287 34Z" fill="url(#tealg)"/>
    <path d="M287 476C340 492 390 520 410 558H287Z" fill="url(#tealg)"/>
    <path d="M573 250C548 330 505 440 478 558H573Z" fill="url(#tealg)"/>
    <path d="M548 0C600 140 540 380 462 558H478C560 380 620 140 566 0Z" fill="url(#swoosh)"/>
    <path d="M520 0C560 120 520 330 440 558H452C536 330 576 120 534 0Z" fill="#ffffff" opacity=".9"/>
    <path d="M573 400C660 360 760 372 860 338V505H573Z" fill="url(#tealg)"/>
    <rect x="573" y="505" width="287" height="53" fill="#e8ebeb"/>
  </svg>

  <div class="panel panel--1">
    <div class="pill" style="top:82px">MAPLEWOOD'S PREMIER MEDISPA</div>
    <p class="abs body-text" style="top:104px;left:14px;width:256px">Lumora Vitality MediSpa is the premier medical spa in Maplewood, TX. We utilize the best equipment available today for laser treatments, dermal fillers, facials, injections, chemical peels and wellness solutions.</p>
    <div class="pill" style="top:166px">WHY CHOOSE OUR MEDISPA?</div>
    <p class="abs body-text" style="top:192px;left:14px;width:256px">Under the supervision of Dr. Elena Hartwell, our medical staff provides state-of-the-art cosmetic treatments to both women and men. Our staff is trained to provide unique medical spa services to help our clients achieve a more youthful look and defy the aging process.</p>
    <div class="pill" style="top:278px">EXCLUSIVE MEMBERSHIPS</div>
    <p class="abs body-text" style="top:304px;left:14px;width:256px">Our exclusive membership packages are tailored for our clients and created to give them an exceptional experience at a discounted price.</p>
    <ul class="abs dot-list" style="top:350px;left:16px">
      <li>SILVER Membership</li>
      <li>GOLD Membership</li>
      <li>PLATINUM Membership</li>
    </ul>
    <p class="abs label-teal" style="top:478px;left:0;width:287px;text-align:center">LEARN MORE AT</p>
    <p class="abs" style="top:497px;left:0;width:287px;text-align:center;font-weight:700;font-size:8.6px">www.LumoraVitalityMedispa.com/memberships</p>
  </div>

  <div class="panel panel--2">
    <div class="photo" role="img" aria-label="Portrait photo of Dr. Elena Hartwell" style="left:80px;top:20px;width:124px;height:124px;border-radius:50%;border:4px solid #8e9396;background:radial-gradient(circle at 50% 40%,#d9b39a 0%,#8a6a55 45%,#4f8d4a 75%)"></div>
    <div class="pill pill--teal" style="left:50%;transform:translateX(-50%);top:152px;white-space:nowrap">DR. ELENA HARTWELL, MD FACS</div>
    <div class="abs" style="top:174px;left:10px;width:198px;font-size:8.3px;line-height:1.36;text-align:justify">
      <p>Rejuvenation and reconstruction of the face are my passion, whether it is to improve one's visual functions or to enhance one's appearance." "I personally perform all of my Injections and CO2 laser treatments because safety and satisfaction are my top priorities?</p>
      <p style="margin-top:5px">"I personally perform all of my Injections and CO2 laser treatments because safety and satisfaction are my top priorities?</p>
      <p style="margin-top:5px">"I was called by God to become a physician at the age of seven years old. I am motivated by a desire to serve others by providing superb medical care. I constantly strive to do my best."</p>
    </div>
    <div class="abs brand" style="top:336px;left:10px;width:176px;font-size:11px"><span class="brand-dot"></span>Lumora Vitality MediSpa</div>
    <p class="abs label-teal" style="top:374px;left:12px">LOCATION</p>
    <div class="abs contact" style="top:386px;left:12px">
      <svg width="7" height="9" viewBox="0 0 7 9"><path d="M3.5 0A3.2 3.2 0 0 0 .3 3.2C.3 5.6 3.5 9 3.5 9S6.7 5.6 6.7 3.2A3.2 3.2 0 0 0 3.5 0Zm0 4.5a1.3 1.3 0 1 1 0-2.6 1.3 1.3 0 0 1 0 2.6Z" fill="#333b3f"/></svg>
      <span>482 W. Maplewood Blvd<br>Suite 210 Maplewood TX 75012</span>
    </div>
    <p class="abs label-teal" style="top:414px;left:12px">SCHEDULE A CONSULTATION</p>
    <div class="abs" style="top:427px;left:12px">
      <div class="contact"><svg width="8" height="8" viewBox="0 0 10 10"><circle cx="5" cy="5" r="4.4" fill="none" stroke="#333b3f"/><path d="M3.4 2.7l.8-.2.6 1.3-.5.4c.3.6.8 1.1 1.4 1.4l.4-.5 1.3.6-.2.8c-1.9.2-4-1.9-3.8-3.8Z" fill="#333b3f"/></svg><span>(555) 410-2280</span></div>
      <div class="contact"><svg width="8" height="8" viewBox="0 0 10 10"><rect x="1" y="3" width="8" height="5" rx="1" fill="#333b3f"/><rect x="3" y="1" width="4" height="3" fill="#333b3f"/></svg><span>(555) 410-2291</span></div>
    </div>
    <div class="abs" style="top:462px;left:12px;font-size:6.6px">
      <div class="contact"><svg width="7" height="6" viewBox="0 0 7 5"><rect width="7" height="5" rx=".6" fill="#333b3f"/></svg><span>renew@elenahartwellmd.com</span></div>
      <div class="contact"><svg width="7" height="7" viewBox="0 0 8 8"><circle cx="4" cy="4" r="3.6" fill="#333b3f"/></svg><span>www.LumoraVitalityMedispa.com</span></div>
    </div>
  </div>

  <div class="panel panel--3">
    <p class="abs" style="top:24px;left:0;width:287px;text-align:center;font-family:'Montserrat',sans-serif;font-weight:500;font-size:10px;letter-spacing:.3px;color:var(--grey)">REFRESH AND REJUVENATE</p>
    <div class="abs brand" style="top:62px;left:0;width:287px;font-size:15px"><span class="brand-dot" style="width:13px;height:13px"></span>Lumora Vitality MediSpa</div>
    <div class="photo" role="img" aria-label="Close-up beauty photo of a woman's face with clear skin" style="left:30px;top:112px;width:257px;height:276px;background:radial-gradient(ellipse at 65% 50%,#f0cdb7 0%,#e6b79c 45%,#f3f4f4 80%)"></div>
    <p class="abs" style="top:398px;left:16px;font-family:'Montserrat',sans-serif;font-weight:700;font-size:16px;color:#0f5a52">FOR WOMEN AND MEN</p>
    <ul class="abs white" style="top:424px;left:18px;list-style:none;font-size:8px;line-height:1.3;columns:2;column-gap:40px;width:230px">
      <li>• Laser Treatments</li><li>• Dermal Fillers</li><li>• Neurotoxins</li>
      <li>• Facials</li><li>• Chemical Peels</li><li>• Wellness Treatments</li>
    </ul>
    <div class="abs" style="top:474px;left:50%;transform:translateX(-50%);width:118px;height:20px;border-radius:10px;background:#fff;display:flex;align-items:center;justify-content:center;gap:5px;font-size:11px;font-weight:600;color:var(--ink)">
      <svg width="10" height="10" viewBox="0 0 10 10"><circle cx="5" cy="5" r="4.4" fill="none" stroke="#333b3f"/><path d="M3.4 2.7l.8-.2.6 1.3-.5.4c.3.6.8 1.1 1.4 1.4l.4-.5 1.3.6-.2.8c-1.9.2-4-1.9-3.8-3.8Z" fill="#333b3f"/></svg>(555) 410-2280
    </div>
    <p class="abs" style="top:524px;left:0;width:287px;text-align:center;font-weight:700;font-size:8.6px">www.LumoraVitalityMedispa.com</p>
  </div>
</section>

<section class="spread spread--inside">
  <svg class="spread-art" viewBox="0 0 860 558" aria-hidden="true">
    <defs>
      <linearGradient id="ip1" x1="0" x2="1"><stop offset="0" stop-color="#d9eef8"/><stop offset=".6" stop-color="#ffffff"/></linearGradient>
      <linearGradient id="itl" x1="0" x2="1"><stop offset="0" stop-color="#22a593"/><stop offset="1" stop-color="#3cc1ad"/></linearGradient>
    </defs>
    <rect x="0" y="0" width="287" height="558" fill="url(#ip1)"/>
    <rect x="0" y="520" width="287" height="38" fill="#3bb3a3"/>
    <rect x="287" y="0" width="287" height="558" fill="#f1f2f2"/>
    <rect x="573" y="0" width="287" height="558" fill="#f4f5f5"/>
    <path d="M287 312C380 284 480 296 573 330V520H287Z" fill="#34a6d7"/>
    <path d="M287 334C380 306 480 316 573 352V520H287Z" fill="#3a3d40"/>
    <path d="M287 346C380 322 480 330 573 362V520H287Z" fill="url(#itl)"/>
    <rect x="287" y="520" width="287" height="38" fill="#e3e5e5"/>
    <path d="M573 372C680 366 780 352 860 320V558H573Z" fill="#5cc0e8"/>
    <path d="M573 384C680 378 780 364 860 334V558H573Z" fill="#ffffff"/>
    <path d="M573 396C680 390 780 378 860 348V558H573Z" fill="url(#itl)"/>
  </svg>

  <div class="panel panel--1">
    <div class="tab">LASER TREATMENTS</div>
    <div class="pill" style="top:56px">Laser Hair Removal</div>
    <p class="abs body-text" style="top:76px;left:10px;width:262px">Laser hair removal is a great solution for those who no longer want to continue shaving, tweezing or waxing to remove unwanted hair. Our innovative laser hair removal treatments can permanently remove unwanted body hair.</p>
    <div class="pill" style="top:134px">IntimaCare</div>
    <p class="abs body-text" style="top:156px;left:10px;width:262px">IntimaCare is an outpatient, minimally invasive, non-hormonal vaginal procedure designed to stimulate new collagen production for healthier tissue. This procedure treats dryness, itchiness, loss of sensation and stress Incontinence.</p>
    <div class="pill" style="top:226px">CO2 Resurfacing</div>
    <p class="abs body-text" style="top:250px;left:10px;width:262px">The CO2 laser is the highest power continuous laser, making it ideal for resurfacing. The wavelengths produced are ideal the energy to be absorbed in the skin and produce excellent results. It reduces wrinkles, age spots, and stimulates collagen production.</p>
    <div class="pill" style="top:322px">IPL Photofacial</div>
    <p class="abs body-text" style="top:348px;left:10px;width:262px">Brown spots, broken capillaries and other fallout from photo aging are easy targets for this laser system, which uses broadband light to repair these defects.</p>
    <div class="pill" style="top:400px">IPL Acne/Rosacea/Spider Vein</div>
    <p class="abs body-text" style="top:424px;left:10px;width:262px">Acne can be treated nonablatively using IPL, a relatively low-energy, short-pulse of broadband light, resulting in an improvement of the skin's appearance with less breakouts. Rosacea and spider veins are also reduced using IPL.</p>
  </div>

  <div class="panel panel--2">
    <div class="tab">INJECTABLES</div>
    <ul class="abs dot-list" style="top:58px;left:24px;columns:3;column-gap:14px;width:240px">
      <li>Smoothara</li><li>Contoura</li><li>Easeline</li>
      <li>Plumera</li><li>Fillara</li><li>PRP</li>
      <li>Velvira</li><li>Volume</li><li>Sculptiva</li>
    </ul>
    <div class="photo" role="img" aria-label="Photo of a smiling woman in a sun hat in a sunny flower field" style="left:44px;top:128px;width:196px;height:172px;border-radius:50%;border:6px solid var(--teal);background:radial-gradient(ellipse at 50% 40%,#f4f4ef 0%,#9ccbe8 55%,#c65b4a 92%)"></div>
    <p class="abs white" style="top:376px;left:0;width:287px;text-align:center;font-family:'Montserrat',sans-serif;font-weight:600;font-size:9px">CLIENT TESTIMONIAL</p>
    <p class="abs white" style="top:396px;left:24px;width:238px;font-size:8px;font-style:italic;line-height:1.4;text-align:justify"><span style="font-size:13px;line-height:0">“</span> Dr. Hartwell has been doing my Smoothara and Fillers for the past year now and I have been very happy with the results. She has a caring, calming touch that has helped me overcome my fear of needles. I can't say enough wonderful things about Dr. Hartwell. <span style="font-size:13px;line-height:0">”</span></p>
    <p class="abs white" style="top:460px;left:24px;font-size:8px;font-weight:700">CLARA <span style="font-weight:400">- HAPPY CLIENT</span></p>
  </div>

  <div class="panel panel--3">
    <div class="tab">FACIALS &amp; CHEMICAL PEELS</div>
    <ul class="abs dot-list" style="top:56px;left:14px;width:130px;font-size:7.6px">
      <li>Microneedling with PRP</li><li>Dermaplane Facial</li><li>Medical Grade Chemical Peel</li>
    </ul>
    <ul class="abs dot-list" style="top:56px;left:160px;font-size:7.6px">
      <li>Facials</li><li>Waxing</li><li>AquaGlow MD</li>
    </ul>
    <div class="tab tab--mid" style="top:126px">WELLNESS TREATMENTS</div>
    <ul class="abs dot-list" style="top:170px;left:24px;font-size:7.6px">
      <li>B-12 Injections</li>
    </ul>
    <ul class="abs tick-list" style="top:186px;left:36px">
      <li>Lipo B - Weight loss</li><li>LipoB + Carnitine - Muscle Building</li>
    </ul>
    <ul class="abs dot-list" style="top:222px;left:24px;font-size:7.6px">
      <li>Hormone Replacement Therapy</li>
    </ul>
    <div class="tab tab--mid" style="top:242px">SKINCARE &amp; DERMA ESSENTIALS</div>
    <div class="abs brand" style="top:300px;left:0;width:287px;font-size:13px"><span class="brand-dot" style="width:12px;height:12px"></span>Lumora Vitality MediSpa</div>
    <div class="abs white contact" style="top:408px;left:0;width:287px;justify-content:center;font-size:7.8px;text-align:left">
      <svg width="7" height="9" viewBox="0 0 7 9"><path d="M3.5 0A3.2 3.2 0 0 0 .3 3.2C.3 5.6 3.5 9 3.5 9S6.7 5.6 6.7 3.2A3.2 3.2 0 0 0 3.5 0Zm0 4.5a1.3 1.3 0 1 1 0-2.6 1.3 1.3 0 0 1 0 2.6Z" fill="#fff"/></svg>
      <span>482 W. Maplewood Blvd<br>Suite 210<br>Maplewood TX 75012</span>
    </div>
    <div class="abs white" style="top:456px;left:0;width:287px;display:flex;justify-content:center;gap:12px;font-size:11px">
      <span>(555) 410-2280</span><span>(555) 410-2291</span>
    </div>
    <div class="abs white" style="top:478px;left:60px;font-size:6.8px;line-height:1.7">
      <div class="contact"><svg width="7" height="6" viewBox="0 0 7 5"><rect width="7" height="5" rx=".6" fill="#fff"/></svg><span>renew@elenahartwellmd.com</span></div>
      <div class="contact"><svg width="7" height="7" viewBox="0 0 8 8"><circle cx="4" cy="4" r="3.6" fill="#fff"/></svg><span>www.LumoraVitalityMedispa.com</span></div>
    </div>
  </div>
</section>

</body>
</html>
```